Business Cards

Business card design for my company.
I would like the card's background colour to be black. You can also see our web site to get an idea of our brand. https://www.dlqmarrowfield.com.au/
- Name
- Email

```html
<!DOCTYPE html>
<html lang="en">
<head>
<meta charset="utf-8">
<title>DLQ Marrowfield – Business Card</title>
<link rel="stylesheet" href="https://fonts.googleapis.com/css2?family=Gelasio:wght@400&family=Fira+Sans:wght@400;600&display=swap">
<style>
  :root {
    --card-black: #000000;
    --brand-green: #0d9143;
    --text-white: #f4f4f4;
  }
  html, body {
    margin: 0;
    padding: 0;
    width: 1200px;
    height: 686px;
    overflow: hidden;
    background: var(--card-black);
  }
  .card {
    position: relative;
    width: 1200px;
    height: 686px;
    background: var(--card-black);
    overflow: hidden;
  }
  .contact {
    position: absolute;
    right: 95px;
    top: 58px;
    text-align: right;
  }
  .contact-name {
    margin: 0;
    font-family: "Gelasio", Georgia, serif;
    font-weight: 400;
    font-size: 56px;
    line-height: 1.1;
    color: var(--brand-green);
  }
  .contact-email {
    margin: 6px 0 0;
    font-family: "Fira Sans", Arial, sans-serif;
    font-weight: 400;
    font-size: 30px;
    line-height: 1.2;
    color: var(--text-white);
  }
  .company-name {
    position: absolute;
    left: 663px;
    width: 450px;
    top: 365px;
    margin: 0;
    text-align: center;
    font-family: "Fira Sans", Arial, sans-serif;
    font-weight: 600;
    font-size: 50px;
    line-height: 1;
    color: var(--text-white);
  }
  .ground-band {
    position: absolute;
    left: 0;
    top: 0;
    width: 1200px;
    height: 686px;
    pointer-events: none;
  }
  .ground-band polygon { fill: var(--brand-green); }
</style>
</head>
<body>
  <main class="card">
    <div class="contact">
      <h1 class="contact-name">Noel Brackett</h1>
      <p class="contact-email">n_noel@DLQ_M.com</p>
    </div>

    <p class="company-name">DLQ Marrowfield</p>

    <svg class="ground-band" viewBox="0 0 1200 686" aria-hidden="true">
      <polygon points="451,686 985,575 1195,686"/>
    </svg>
  </main>
</body>
</html>
```